Bref créative
Clearwave Imaging
Business Cards, Letter Head, Envelopes
Professional
Dorothea Kessling, RDMS, RVT
President
41672 Bramblewood Ave., # 208
Fernhaven, CA 91387
dorothea@clear-wave-im.com
www.clear-wave-im.com
Ultrasound Studies Performed:
Abdomen, Renal, Thyroid, Breast, Scrotal, GYN/OB/NT, Vascular: LE & UE Venous and Arterial, ABI, Carotid, Renal Artery, Vein Mapping, Hemodialysis Access Graft
We are launching our business card, letter head, envelopes and fax project.

```html
<!DOCTYPE html>
<html lang="en">
<head>
<meta charset="utf-8">
<title>Clearwave Imaging – Stationery Set</title>
<link rel="stylesheet" href="https://fonts.googleapis.com/css2?family=Open+Sans:wght@400;600;700&display=swap">
<style>
  :root{
    --bg:#2b2b2b;
    --paper:#ffffff;
    --blue:#1f6fd1;
    --blue-dark:#1457ad;
    --ink:#6a6a6a;
    --ink-light:#9a9a9a;
  }
  *{box-sizing:border-box;margin:0;padding:0}
  html,body{width:1200px;height:845px;overflow:hidden;background:var(--bg);font-family:"Open Sans",Arial,sans-serif}
  .canvas{position:relative;width:1200px;height:845px}
  .sheet{position:absolute;background:var(--paper);box-shadow:0 4px 14px rgba(0,0,0,.45);overflow:hidden}
  .brand{display:flex;align-items:center;gap:6px;color:var(--blue);font-weight:700;line-height:1.05}
  .brand-dot{width:10px;height:10px;border-radius:50%;background:var(--blue);flex:none}
  .brand-name{font-size:15px}

  /* Letterhead */
  .letterhead{left:60px;top:163px;width:528px;height:600px}
  .letterhead .brand{position:absolute;left:50%;top:26px;transform:translateX(-50%);white-space:nowrap}
  .letterhead .brand-name{font-size:18px}
  .letterhead-footer{position:absolute;left:0;right:0;bottom:24px;text-align:center;color:var(--ink-light);font-size:8px;line-height:1.5}
  .letterhead-band{position:absolute;left:0;right:0;bottom:0;height:11px;background:var(--blue)}

  /* Business cards */
  .card-back{left:605px;top:166px;width:187px;height:130px;background:var(--blue)}
  .card-back .brand{position:absolute;right:10px;top:12px;color:#fff;white-space:nowrap}
  .card-back .brand-dot{background:#fff;width:7px;height:7px}
  .card-back .brand-name{font-size:10px}
  .studies{position:absolute;left:12px;top:48px;right:12px;color:#dbe8fb;font-size:5.6px;line-height:1.45}
  .studies strong{display:block;font-weight:600;color:#fff}
  .card-back-band{position:absolute;left:0;right:0;bottom:0;height:10px;background:var(--blue-dark)}

  .card-front{left:806px;top:166px;width:192px;height:130px}
  .card-front .brand{position:absolute;right:10px;top:12px}
  .card-front .brand-dot{width:7px;height:7px}
  .card-front .brand-name{font-size:10px}
  .person{position:absolute;left:12px;top:36px;color:var(--ink);font-size:6px;line-height:1.35}
  .person .name{font-weight:600;color:#444}
  .contact{position:absolute;left:12px;top:64px;color:var(--ink-light);font-size:5.5px;line-height:1.5}
  .card-front-band{position:absolute;left:0;right:0;bottom:0;height:8px;background:var(--blue)}

  /* Envelope */
  .envelope-front{left:605px;top:300px;width:533px;height:204px}
  .envelope-front .brand{position:absolute;left:20px;top:14px;white-space:nowrap}
  .envelope-front .brand-name{font-size:13px}
  .return-address{position:absolute;left:20px;top:60px;color:var(--ink-light);font-size:7.5px;line-height:1.5}
  .return-address span{display:inline-block;width:10px;color:var(--blue)}
  .envelope-front-band{position:absolute;left:0;right:0;bottom:0;height:10px;background:var(--blue)}

  .envelope-back{left:605px;top:520px;width:533px;height:200px}
  .envelope-flap{position:absolute;left:0;top:0;width:533px;height:80px}
  .flap-url{position:absolute;left:0;right:0;top:24px;text-align:center;color:#fff;font-size:7.5px}
</style>
</head>
<body>
<main class="canvas">

  <section class="sheet letterhead">
    <div class="brand"><span class="brand-dot"></span><span class="brand-name">Clearwave Imaging</span></div>
    <div class="letterhead-footer">
      41672 Bramblewood Ave., # 208 &nbsp;Fernhaven, CA 91387<br>
      P. 555-210-0142 &nbsp;E. dorothea@clear-wave-im.com<br>
      www.clear-wave-im.com
    </div>
    <div class="letterhead-band"></div>
  </section>

  <section class="sheet card-back">
    <div class="brand"><span class="brand-dot"></span><span class="brand-name">Clearwave Imaging</span></div>
    <p class="studies"><strong>Ultrasound Studies Performed:</strong>Abdomen, Renal, Thyroid, Breast, Scrotal, GYN/OB/NT, Vascular: LE &amp; UE Venous and Arterial, ABI, Carotid, Renal Artery, Vein Mapping, Hemodialysis Access Graft</p>
    <div class="card-back-band"></div>
  </section>

  <section class="sheet card-front">
    <div class="brand"><span class="brand-dot"></span><span class="brand-name">Clearwave<br>Imaging</span></div>
    <div class="person"><div class="name">Dorothea Kessling, RDMS, RVT</div><div>President</div></div>
    <div class="contact">
      41672 Bramblewood Ave., # 208<br>
      Fernhaven, CA 91387<br>
      P. 555-210-0142<br>
      dorothea@clear-wave-im.com<br>
      www.clear-wave-im.com
    </div>
    <div class="card-front-band"></div>
  </section>

  <section class="sheet envelope-front">
    <div class="brand"><span class="brand-dot"></span><span class="brand-name">Clearwave Imaging</span></div>
    <div class="return-address">
      <span>A.</span>41672 Bramblewood Ave., # 208<br>
      <span></span>Fernhaven, CA 91387<br>
      <span>P.</span>555-210-0142<br>
      <span>E.</span>dorothea@clear-wave-im.com
    </div>
    <div class="envelope-front-band"></div>
  </section>

  <section class="sheet envelope-back">
    <svg class="envelope-flap" viewBox="0 0 533 80" preserveAspectRatio="none" aria-hidden="true">
      <path d="M0 0 H533 V22 Q500 62 440 64 H93 Q33 62 0 22 Z" fill="var(--blue-dark)"/>
      <path d="M0 0 H533 V16 Q500 54 440 56 H93 Q33 54 0 16 Z" fill="var(--blue)"/>
    </svg>
    <div class="flap-url">www.clear-wave-im.com</div>
  </section>

</main>
</body>
</html>
```